Visitenkarten-Design für Boutique-Unternehmensberatung
Zielgruppe
Boutique Unternehmensberatung für die Chemische Industrie. Wir unterstützen Unternehmen, die Beziehung zu Ihren Händlern zu optimieren.
Vorläufige Website handelsbruecke-nord.de kann ggf weitere Einblicke geben. Hinweis: Diese Website wurde bisher noch nicht professionell erstellt.
Aufgabenstellung
Die Visitenkarte sollte vertrauenserweckend und seriös wirken. Zeitgleich aber auch modern.

```html
<!DOCTYPE html>
<html lang="de">
<head>
<meta charset="utf-8">
<title>Visitenkarte – Handelsbrücke Nord</title>
<link href="https://fonts.googleapis.com/css2?family=Montserrat:wght@400;500;600;700&display=swap" rel="stylesheet">
<style>
  :root {
    --brand-blue: #17568e;
    --white: #ffffff;
    --page: #ffffff;
    --photo-dark: #5a6f86;
    --photo-light: #c9b7a6;
  }
  * { box-sizing: border-box; margin: 0; padding: 0; }
  html, body {
    width: 1200px; height: 738px; overflow: hidden;
    background: var(--page);
    font-family: "Montserrat", Arial, sans-serif;
  }
  .canvas { position: relative; width: 1200px; height: 738px; }
  .card {
    position: absolute; top: 233px;
    width: 411px; height: 266px;
    box-shadow: 6px 7px 6px rgba(0,0,0,0.45);
    overflow: hidden;
  }
  .card--front { left: 155px; background: var(--brand-blue); }
  .card--back { left: 631px; background: var(--white); }

  .front-brand {
    position: absolute; inset: 0;
    display: flex; flex-direction: column; align-items: center; justify-content: center;
    gap: 14px; color: var(--white);
  }
  .front-brand__dot { width: 66px; height: 66px; border-radius: 50%; background: var(--white); }
  .front-brand__name { font-size: 19px; font-weight: 700; line-height: 1.15; text-align: center; }

  .back-wave { position: absolute; left: 0; top: 0; width: 411px; height: 266px; }
  .holder { position: absolute; left: 21px; top: 20px; color: var(--white); }
  .holder__name { font-size: 22px; font-weight: 700; letter-spacing: 0.5px; line-height: 1.1; }
  .holder__role { font-size: 13.5px; font-weight: 400; margin-top: 2px; }

  .contact-list { list-style: none; }
  .contact-list li {
    display: flex; align-items: center; gap: 6px;
    font-size: 11px; line-height: 16.5px;
  }
  .contact-list svg { width: 11px; height: 11px; flex: none; }
  .holder .contact-list { margin-top: 10px; color: var(--white); }

  .portrait {
    position: absolute; left: 278px; top: 28px;
    width: 92px; height: 92px; border-radius: 50%;
    border: 4px solid var(--white);
    background: linear-gradient(160deg, var(--photo-light), var(--photo-dark));
  }

  .company { position: absolute; left: 21px; top: 152px; color: var(--brand-blue); }
  .company__name { font-size: 11px; font-weight: 600; line-height: 16px; }
  .company__address { font-size: 11px; line-height: 18px; }
  .company .contact-list { margin-top: 13px; }

  .back-brand {
    position: absolute; left: 286px; top: 184px; width: 104px;
    color: var(--brand-blue); font-size: 12px; font-weight: 700;
    line-height: 1.15; text-align: center;
  }
  .back-brand__dot {
    width: 34px; height: 34px; border-radius: 50%;
    background: var(--brand-blue); margin: 0 auto 6px;
  }
  .accent-bar {
    position: absolute; left: 0; bottom: 0;
    width: 187px; height: 9px; background: var(--brand-blue);
  }
</style>
</head>
<body>
<div class="canvas">
  <section class="card card--front">
    <div class="front-brand">
      <div class="front-brand__dot"></div>
      <div class="front-brand__name">Handelsbrücke<br>Nord</div>
    </div>
  </section>

  <section class="card card--back">
    <svg class="back-wave" viewBox="0 0 411 266" aria-hidden="true">
      <path d="M0 0 H411 V42 C340 85 220 128 80 124 Q30 122 0 120 Z" fill="var(--brand-blue)"/>
    </svg>

    <div class="holder">
      <h1 class="holder__name">Jonas Hartwig</h1>
      <p class="holder__role">Geschäftsführer / Managing Director</p>
      <ul class="contact-list">
        <li><svg viewBox="0 0 12 12"><circle cx="6" cy="6" r="6" fill="#fff"/><rect x="4" y="2.5" width="4" height="7" rx="0.8" fill="none" stroke="#17568e" stroke-width="1"/></svg>+49 171 / 5550 2231</li>
        <li><svg viewBox="0 0 12 12"><circle cx="6" cy="6" r="6" fill="#fff"/><rect x="3" y="4" width="6" height="4.2" fill="none" stroke="#17568e" stroke-width="0.9"/><path d="M3 4 L6 6.4 L9 4" fill="none" stroke="#17568e" stroke-width="0.9"/></svg>jh@handelsbruecke-nord.de</li>
      </ul>
    </div>

    <div class="portrait" role="img" aria-label="Porträtfoto des Geschäftsführers"></div>

    <div class="company">
      <p class="company__name">Handelsbrücke Nord GmbH</p>
      <p class="company__address">Lindenweg 12 · 64283 Darmstadt</p>
      <ul class="contact-list">
        <li><svg viewBox="0 0 12 12"><circle cx="6" cy="6" r="6" fill="#17568e"/><path d="M4 3 L5.2 4.4 L4.6 5.3 Q5.4 6.8 6.7 7.4 L7.6 6.8 L9 8 L8.2 9 Q5.5 9 3.2 4.2 Z" fill="#fff"/></svg>+49 6151 / 555 0192</li>
        <li><svg viewBox="0 0 12 12"><circle cx="6" cy="6" r="6" fill="#17568e"/><rect x="3" y="4" width="6" height="4.2" fill="none" stroke="#fff" stroke-width="0.9"/><path d="M3 4 L6 6.4 L9 4" fill="none" stroke="#fff" stroke-width="0.9"/></svg>info@handelsbruecke-nord.de</li>
        <li><svg viewBox="0 0 12 12"><circle cx="6" cy="6" r="6" fill="#17568e"/><circle cx="6" cy="6" r="3.2" fill="none" stroke="#fff" stroke-width="0.8"/><path d="M2.8 6 H9.2 M6 2.8 V9.2" stroke="#fff" stroke-width="0.6"/></svg>www.handelsbruecke-nord.de</li>
      </ul>
    </div>

    <div class="back-brand">
      <div class="back-brand__dot"></div>
      Handelsbrücke<br>Nord
    </div>

    <div class="accent-bar"></div>
  </section>
</div>
</body>
</html>
```